Need a mailer box for a 3 tier walnut display stand

Need help creating a mailer box for a 3 tier walnut display stand. Brand is Timberline Nook. I like the Kraft Brown box look. I have attached an image of a box that I really like with the product in stencil in white and company logo in black.

Colors

Designer to choose colors to be used in the design.

```html
<!DOCTYPE html>
<html lang="en">
<head>
<meta charset="utf-8">
<title>Timberline Nook – 3 Tier Walnut Display Stand Mailer Box</title>
<link rel="stylesheet" href="https://fonts.googleapis.com/css2?family=Inter+Tight:wght@500;700;800;900&family=Outfit:wght@400;500&display=swap">
<style>
  :root {
    --kraft: #c49a6c;
    --ink: #111111;
    --fold: #6f5a43;
    --paper: #ffffff;
    --wood-dark: #1c1c1c;
    --wood-mid: #4a4a4a;
    --stencil: rgba(255,255,255,0.28);
  }
  * { margin: 0; padding: 0; box-sizing: border-box; }
  html, body { width: 1200px; height: 1000px; overflow: hidden; background: var(--paper); }
  .dieline { position: relative; width: 1200px; height: 1000px; font-family: "Inter Tight", Arial, sans-serif; color: var(--ink); }
  .panel { position: absolute; background: var(--kraft); border: 1px solid var(--fold); }
  .panel-back   { left: 307px; top: 100px; width: 600px; height: 201px; }
  .panel-left   { left: 107px; top: 300px; width: 201px; height: 201px; }
  .panel-top    { left: 307px; top: 300px; width: 600px; height: 201px; }
  .panel-right  { left: 907px; top: 300px; width: 200px; height: 201px; }
  .panel-front  { left: 307px; top: 500px; width: 600px; height: 201px; }
  .panel-bottom { left: 307px; top: 700px; width: 600px; height: 200px; }

  .wood-art { position: absolute; left: 0; top: 0; width: 1200px; height: 1000px; pointer-events: none; }
  .product-stencil { position: absolute; left: 0; top: 0; width: 1200px; height: 1000px; pointer-events: none; }

  .brand-name { position: absolute; font-family: "Inter Tight", Arial, sans-serif; font-weight: 800; text-transform: uppercase; text-align: center; line-height: 1.05; letter-spacing: 0.04em; }
  .brand-left  { left: 107px; top: 352px; width: 200px; font-size: 34px; color: var(--ink); }
  .brand-right { left: 930px; top: 368px; width: 160px; font-size: 26px; color: var(--paper); }
  .brand-top   { left: 315px; top: 345px; width: 106px; font-size: 13px; color: var(--ink); }
  .brand-front { left: 322px; top: 648px; width: 106px; font-size: 13px; color: var(--ink); }

  .care-icons { position: absolute; left: 328px; top: 248px; display: flex; gap: 9px; }
  .care-icons svg { width: 33px; height: 33px; }

  .contents-label { position: absolute; left: 767px; top: 124px; width: 118px; height: 81px; border: 1.5px solid var(--ink); transform: rotate(180deg); padding: 7px 6px; font-size: 7.5px; line-height: 1.35; text-align: center; }
  .contents-label strong { display: block; font-weight: 800; font-size: 8px; }
  .contents-label span { display: block; font-weight: 500; }
  .contents-label .gap { height: 6px; }

  .dimensions-title { position: absolute; left: 338px; top: 392px; font-size: 9.5px; font-weight: 800; }
  .dimensions-art { position: absolute; left: 325px; top: 424px; width: 96px; height: 42px; background: linear-gradient(180deg, rgba(17,17,17,0.35), rgba(17,17,17,0.15)); }

  .tiers-title { position: absolute; left: 434px; top: 325px; font-size: 21px; font-weight: 900; }
  .tiers-rule { position: absolute; left: 434px; top: 351px; width: 231px; border-top: 1.5px solid var(--ink); }
  .tier-card { position: absolute; top: 358px; width: 76px; height: 75px; border: 1.5px solid var(--ink); }
  .tier-card.small  { left: 434px; }
  .tier-card.medium { left: 512px; }
  .tier-card.large  { left: 590px; }
  .tier-number { position: absolute; left: -1px; top: -1px; width: 12px; height: 12px; background: var(--ink); color: var(--kraft); font-size: 8px; font-weight: 700; text-align: center; line-height: 12px; }
  .tier-size { position: absolute; left: 22px; top: 2px; font-size: 9px; font-weight: 800; }
  .tier-art { position: absolute; left: 8px; top: 24px; right: 8px; bottom: 12px; background: linear-gradient(180deg, rgba(17,17,17,0.3), rgba(17,17,17,0.12)); }

  .product-title { position: absolute; left: 330px; top: 518px; font-size: 42px; line-height: 0.95; letter-spacing: 0; white-space: nowrap; }
  .product-title .line-light { display: block; font-weight: 500; }
  .product-title .line-bold { display: block; font-weight: 900; }

  .bottom-label { position: absolute; left: 802px; top: 856px; font-family: "Outfit", Arial, sans-serif; font-size: 21px; font-weight: 400; }

  .annotation { position: absolute; font-family: "Outfit", Arial, sans-serif; font-size: 21px; font-weight: 400; color: var(--ink); }
  .annotation-back  { left: 1010px; top: 174px; }
  .annotation-left  { left: 111px; top: 240px; }
  .annotation-front { left: 157px; top: 586px; }
  .annotation-right { left: 980px; top: 511px; }
  .annotation-lines { position: absolute; left: 0; top: 0; width: 1200px; height: 1000px; pointer-events: none; }
</style>
</head>
<body>
<main class="dieline">
  <section class="panel panel-back"></section>
  <section class="panel panel-left"></section>
  <section class="panel panel-top"></section>
  <section class="panel panel-right"></section>
  <section class="panel panel-front"></section>
  <section class="panel panel-bottom"></section>

  <svg class="wood-art" viewBox="0 0 1200 1000" role="img" aria-label="Dark weathered wood plank photograph wrapping the right side panel">
    <defs>
      <linearGradient id="woodTone" x1="0" y1="0" x2="1" y2="1">
        <stop offset="0" stop-color="var(--wood-mid)"/>
        <stop offset="0.5" stop-color="var(--wood-dark)"/>
        <stop offset="1" stop-color="var(--wood-mid)"/>
      </linearGradient>
    </defs>
    <polygon fill="url(#woodTone)" points="693,213 907,258 907,300 1107,300 1107,500 643,500 652,462 700,440 690,425 712,384 675,378 705,350 712,325 693,213"/>
  </svg>

  <div class="brand-name brand-left">Timber&shy;line<br>Nook</div>
  <div class="brand-name brand-right">Timberline<br>Nook</div>

  <div class="care-icons" aria-label="Handling symbols">
    <svg viewBox="0 0 33 33"><rect x="1" y="1" width="31" height="31" fill="none" stroke="#111" stroke-width="2"/><path d="M16.5 7 L24 20 H9 Z" fill="none" stroke="#111" stroke-width="2.5"/></svg>
    <svg viewBox="0 0 33 33"><rect x="1" y="1" width="31" height="31" fill="none" stroke="#111" stroke-width="2"/><path d="M11 6v18M22 6v18M7 12l4-6 4 6M18 12l4-6 4 6M6 28h21" fill="none" stroke="#111" stroke-width="2"/></svg>
    <svg viewBox="0 0 33 33"><rect x="1" y="1" width="31" height="31" fill="none" stroke="#111" stroke-width="2"/><path d="M6 15a10.5 9 0 0 1 21 0Z" fill="#111"/><path d="M16.5 15v9a2.5 2.5 0 0 1-5 0" fill="none" stroke="#111" stroke-width="2"/></svg>
    <svg viewBox="0 0 33 33"><rect x="1" y="1" width="31" height="31" fill="none" stroke="#111" stroke-width="2"/><path d="M16.5 6l7 5v9l-7 5-7-5v-9Z" fill="#111"/></svg>
  </div>

  <div class="contents-label">
    <strong>THIS BOX CONTAINS:</strong>
    <span>3 DISPLAY STANDS</span>
    <div class="gap"></div>
    <strong>MATERIALS:</strong>
    <span>WALNUT PLANKS</span>
    <span>METAL FRAMES</span>
  </div>

  <div class="brand-name brand-top">Timberline<br>Nook</div>
  <div class="dimensions-title">DIMENSIONS</div>
  <div class="dimensions-art" role="img" aria-label="Line drawing of the three stacked display stands"></div>

  <div class="tiers-title">3 TIERS</div>
  <div class="tiers-rule"></div>
  <div class="tier-card small"><span class="tier-number">1</span><span class="tier-size">SMALL</span><div class="tier-art" role="img" aria-label="Line drawing of the small stand"></div></div>
  <div class="tier-card medium"><span class="tier-number">2</span><span class="tier-size">MEDIUM</span><div class="tier-art" role="img" aria-label="Line drawing of the medium stand"></div></div>
  <div class="tier-card large"><span class="tier-number">3</span><span class="tier-size">LARGE</span><div class="tier-art" role="img" aria-label="Line drawing of the large stand"></div></div>

  <svg class="product-stencil" viewBox="0 0 1200 1000" role="img" aria-label="White stencil drawing of the three tier walnut display stand">
    <defs>
      <linearGradient id="stencilTone" x1="0" y1="0" x2="0" y2="1">
        <stop offset="0" stop-color="#ffffff" stop-opacity="0.28"/>
        <stop offset="1" stop-color="#ffffff" stop-opacity="0.12"/>
      </linearGradient>
    </defs>
    <polygon fill="url(#stencilTone)" points="720,550 887,550 887,690 615,690 615,608 668,608 668,582 720,582"/>
  </svg>

  <h1 class="product-title"><span class="line-light">3 TIER WALNUT</span><span class="line-bold">DISPLAY STAND</span></h1>
  <div class="brand-name brand-front">Timberline<br>Nook</div>

  <div class="bottom-label">Bottom</div>

  <div class="annotation annotation-back">Back</div>
  <div class="annotation annotation-left">Left Side</div>
  <div class="annotation annotation-front">Front</div>
  <div class="annotation annotation-right">Right Side</div>
  <svg class="annotation-lines" viewBox="0 0 1200 1000" fill="none" stroke="#111" stroke-width="1">
    <path d="M1060 200H920M925 197l-5 3 5 3"/>
    <path d="M111 266H225V294M222 289l3 5 3-5"/>
    <path d="M157 612H299M294 609l5 3-5 3"/>
    <path d="M1085 540H945V511M942 516l3-5 3 5"/>
  </svg>
</main>
</body>
</html>
```